Creation d’une etiquette pour pots de confiture d’orange
Besoins
Nous souhaitons une étiquettes design sur fond transparent.
Nous cultivons des oranges en Sardaigne et voulons commercialiser une confiture artisanale faite à la main.
La marque de la confiture serait éventuellement ''Corsetta''
Les messages que nous voulons passer sont :
- fraicheur: confiture faite avec les fruits de saison à peine cueillis
- circuit court: confiture faite par le planteur
- Etiquette à faire avec slogans en Italien
- Sardaigne: oasis écologique
- made in italy avec drapeau italien
Public visé : épicerie fine, vente internet et vente privée
Pot vertical cylindre de h110x73 mm avec couvercle noir
On serait ravis de travailler avec vous ;)
N'hésitez pas à nous contacter pour d'autres info
Baptiste et Marie-Solène
Description de l'entreprise
Entreprise familiale agricole en Sardaigne
La cible
épiceries fines, ventes privées, ventes internet
Couleurs, favoris et autres exigences:
-Orange, Vert
-Vert blanc rouge

```html
<!DOCTYPE html>
<html lang="it">
<head>
<meta charset="utf-8">
<title>Corsetta – Oranges de Sardaigne</title>
<link rel="stylesheet" href="https://fonts.googleapis.com/css2?family=Quicksand:wght@400;500&display=swap">
<style>
  :root {
    --orange: #f39020;
    --white: #ffffff;
    --green: #2e9a3c;
    --red: #e0322b;
    --line: rgba(255,255,255,0.85);
  }
  * { margin: 0; padding: 0; box-sizing: border-box; }
  html, body { width: 1200px; height: 849px; overflow: hidden; }
  body { background: var(--orange); font-family: "Quicksand", sans-serif; color: var(--white); }
  .label { position: relative; width: 1200px; height: 849px; }
  .brand-rule { position: absolute; top: 176px; height: 3px; width: 70px; }
  .brand-rule--green { left: 392px; background: var(--green); }
  .brand-rule--red { right: 392px; background: var(--red); }
  .brand-name {
    position: absolute; top: 140px; left: 0; width: 100%;
    text-align: center; font-size: 56px; font-weight: 500; line-height: 1;
    letter-spacing: 1px;
  }
  .brand-origin {
    position: absolute; top: 212px; left: 0; width: 100%;
    text-align: center; font-size: 16px; font-weight: 400; letter-spacing: 1.5px;
  }
  .connector { position: absolute; left: 599px; width: 2px; background: var(--line); }
  .connector--top { top: 240px; height: 70px; }
  .connector--bottom { top: 538px; height: 112px; }
  .seal { position: absolute; left: 470px; top: 270px; width: 260px; height: 260px; overflow: visible; }
  .flag-bar { position: absolute; top: 668px; left: 450px; width: 300px; height: 6px; display: flex; }
  .flag-bar span { flex: 1; }
  .flag-bar .green { background: var(--green); }
  .flag-bar .white { background: var(--white); }
  .flag-bar .red { background: var(--red); }
  .made-in {
    position: absolute; top: 688px; left: 0; width: 100%;
    text-align: center; font-size: 13px; font-weight: 500;
  }
</style>
</head>
<body>
<main class="label">
  <div class="brand-rule brand-rule--green"></div>
  <div class="brand-rule brand-rule--red"></div>
  <h1 class="brand-name">Corsetta</h1>
  <p class="brand-origin">ORANGES DE SARDAIGNE</p>
  <div class="connector connector--top"></div>

  <svg class="seal" viewBox="0 0 260 260" aria-label="Marmellata fatta in casa fatta a mano">
    <defs>
      <path id="seal-arc" d="M 40 70 A 105 105 0 0 0 190 225"/>
    </defs>
    <circle cx="130" cy="130" r="82" fill="none" stroke="#ffffff" stroke-width="2"/>
    <text font-family="Quicksand, sans-serif" font-size="14" font-weight="500" fill="#ffffff" letter-spacing="1">
      <textPath href="#seal-arc">MARMELLATA FATTA IN CASA FATTA A MANO</textPath>
    </text>
  </svg>

  <div class="connector connector--bottom"></div>
  <div class="flag-bar"><span class="green"></span><span class="white"></span><span class="red"></span></div>
  <p class="made-in">Made in Italy</p>
</main>
</body>
</html>
```